i would like a business card to leave with customers and potential customers for electrical work and for the supply and install of reverse cycle airconditioning in the domestic and commercial market.
I own my own business and im a sole trader. I have an a'class electrical lisence and also a refrigeration lisence so i am
able to offer complete installations in airconditioning by a fully qualified and lisenced tradesman.
im looking for something that comes across as unique and professional.
i had the coluor black and some gold in mind but open to any coluors.
something like Beacon Electrical & Refrigeration
or Beacon Air.
i will use this design on a business card to advertise through summer to help generate installs through the busy season.

Target Market(s)

Mainly domestic house holds through summer who are in need of airconditioning and reliable information to acomadate thier cooling and heating requirements

Industry/Entity Type

Electrical

Requirements
Must have
• Business name- Beacon
My name- Peter Wollaston
My mobile no- 0457 819 302
My email- prwollaston@tarvel.com.au
Installation & Decomissioning of aiconditioning split systems
LIC NO: KTR 407516
Nice to have
• Beacon Electrical & Refrigeration

```html
<!DOCTYPE html>
<html lang="en">
<head>
<meta charset="utf-8">
<title>Beacon Electrical &amp; Refrigeration – Business Card</title>
<link rel="stylesheet" href="https://fonts.googleapis.com/css2?family=Source+Sans+3:wght@400&family=Noto+Sans:wght@400&display=swap">
<style>
  :root {
    --page: #ffffff;
    --charcoal-deep: #2b2b2c;
    --charcoal-mid: #4a4a4c;
    --gold: #d9b65c;
    --gold-soft: #e8d08e;
    --gold-pale: #fbf6e6;
    --ink: #111111;
    --ink-grey: #555555;
    --shadow: rgba(0, 0, 0, 0.28);
  }
  * { margin: 0; padding: 0; box-sizing: border-box; }
  html, body {
    width: 1060px; height: 1200px; overflow: hidden;
    background: var(--page);
  }
  .sheet { position: relative; width: 1060px; height: 1200px; }

  .card {
    position: absolute; left: 41px; width: 978px; height: 555px;
    border-radius: 19px; overflow: hidden;
    box-shadow: 0 2px 8px var(--shadow);
  }
  .card--front {
    top: 41px;
    background: radial-gradient(ellipse at 50% 55%, var(--charcoal-mid) 0%, var(--charcoal-deep) 75%);
  }
  .card--back {
    top: 602px;
    background: radial-gradient(ellipse at 50% 50%, var(--gold-pale) 0%, var(--gold-soft) 45%, var(--gold) 90%);
  }
  .card__swooshes { position: absolute; inset: 0; width: 100%; height: 100%; }

  .wordmark {
    position: absolute; top: 190px; left: 0; width: 100%; text-align: center;
    font-family: "Source Sans 3", sans-serif; font-weight: 400; font-size: 118px;
    line-height: 1; letter-spacing: 0.12em; text-indent: 0.12em;
    color: var(--gold);
  }

  .front-name {
    position: absolute; top: 344px; left: 0; width: 100%; text-align: center;
    font-family: "Source Sans 3", sans-serif; font-size: 36px; color: var(--gold-soft);
  }

  .services {
    position: absolute; top: 152px; left: 0; width: 968px; text-align: center;
    font-family: "Source Sans 3", sans-serif; font-size: 37px; line-height: 53px;
    color: var(--ink);
  }
  .contact {
    position: absolute; top: 325px; left: 0; width: 968px; text-align: center;
    font-family: "Noto Sans", sans-serif; font-size: 24px; line-height: 31px;
    color: var(--ink-grey);
  }
  .authorised {
    position: absolute; left: 810px; top: 228px; width: 150px; text-align: center;
    font-family: "Source Sans 3", sans-serif; font-size: 31px; color: var(--ink);
  }
  .authorised svg { display: block; margin: 0 auto 14px; }
  .licence {
    position: absolute; top: 500px; left: 0; width: 974px; text-align: center;
    font-family: "Source Sans 3", sans-serif; font-size: 37px; color: var(--ink);
  }
</style>
</head>
<body>
<main class="sheet">

  <section class="card card--front">
    <svg class="card__swooshes" viewBox="0 0 978 555" preserveAspectRatio="none" aria-hidden="true">
      <defs>
        <linearGradient id="goldSweep" x1="0" x2="1" y1="0" y2="0">
          <stop offset="0" stop-color="#d4ae55"/>
          <stop offset="0.5" stop-color="#fffbee"/>
          <stop offset="1" stop-color="#d4ae55"/>
        </linearGradient>
      </defs>
      <path d="M0 139 Q489 40 978 139 L978 155 Q489 95 0 155 Z" fill="url(#goldSweep)"/>
      <path d="M0 404 Q489 465 978 404 L978 420 Q489 540 0 420 Z" fill="url(#goldSweep)"/>
    </svg>
    <p class="wordmark">Beacon</p>
    <p class="front-name">Beacon Electrical &amp; Refrigeration</p>
  </section>

  <section class="card card--back">
    <svg class="card__swooshes" viewBox="0 0 978 556" preserveAspectRatio="none" aria-hidden="true">
      <defs>
        <linearGradient id="darkSweep" x1="0" x2="1" y1="0" y2="0">
          <stop offset="0" stop-color="#262627"/>
          <stop offset="0.5" stop-color="#4d4d50"/>
          <stop offset="1" stop-color="#262627"/>
        </linearGradient>
      </defs>
      <path d="M0 152 Q489 40 978 152 L978 172 Q489 70 0 172 Z" fill="url(#darkSweep)"/>
      <path d="M0 404 Q489 455 978 404 L978 430 Q489 505 0 430 Z" fill="url(#darkSweep)"/>
    </svg>

    <div class="services">
      <p>Beacon Electrical &amp; Refrigeration</p>
      <p>Installation &amp; Decomissioning</p>
      <p>of ariconditioning split systems</p>
    </div>

    <div class="contact">
      <p>Peter Wollaston</p>
      <p>Mob.: 0457 819 302</p>
      <p>email: prwollaston@tarvel.com.au</p>
    </div>

    <div class="authorised">
      <svg width="104" height="104" viewBox="0 0 104 104" aria-hidden="true">
        <rect x="1" y="1" width="102" height="102" fill="none" stroke="#8a7a50" stroke-width="1.2"/>
        <path d="M4 50 L38 86 L100 4" fill="none" stroke="#8a7a50" stroke-width="1.2"/>
      </svg>
      <p>Authorised</p>
    </div>

    <p class="licence">LIC NO: KTR 407516</p>
  </section>

</main>
</body>
</html>
```